A5 Flyer for Financial Services Business

I am after a re-design of our business flyer to fit in with our new branding style and logo colour scheme. Wanting something with a bit of designer flair that I could not create myself. I have included the flyer which I created which lacks style so dazzle me.

I want to use the same content.

Text for main body of flyer is

Are you a small business owner, tradie or PAVC Service Provider struggling to stay on top of your bookkeeping and compliance obligations? If so we would love to help you get back on track and take control of your business finances so that you can make informed business decisions and focus on what you do best.

We have over 20 years industry experience and, as a small business ourselves, we are able to offer our clients a personal bookkeeping solution tailored to meet the needs of your business.

Accounts Payable | Accounts Receivable
Customer Invoicing
Bank and Credit Card Reconciliations
Payroll | Superannuation | Payroll Tax
Business Activity | Instalment Activity Statements
Regular Financial Reports
Ledgra and Tallybook Set-Up and Training

```html
<!DOCTYPE html>
<html lang="en">
<head>
<meta charset="utf-8">
<title>Even Ledger Financial Services – Bookkeeping Flyer</title>
<link rel="stylesheet" href="https://fonts.googleapis.com/css2?family=Poppins:wght@600;700;800&family=Montserrat:wght@400;500&display=swap">
<style>
  :root {
    --teal: #148f96;
    --teal-dark: #0f7a80;
    --grey: #96979b;
    --grey-light: #e8e8e8;
    --ink: #111111;
    --body: #1d1d1d;
    --white: #ffffff;
    --page: #e9e9e9;
  }
  * { margin: 0; padding: 0; box-sizing: border-box; }
  html, body { width: 1200px; height: 1067px; overflow: hidden; background: var(--page); }
  .stage { position: relative; width: 1200px; height: 1067px; overflow: hidden; }
  .flyer {
    position: absolute; left: 237px; top: 19px;
    width: 981px; height: 1391px;
    transform: scale(0.74); transform-origin: top left;
    background: var(--white); overflow: hidden;
    font-family: "Montserrat", sans-serif;
  }
  .abs { position: absolute; }
  .shape-layer { position: absolute; inset: 0; width: 981px; height: 1391px; }

  .hero-photo {
    left: 110px; top: 215px; width: 871px; height: 607px;
    background: linear-gradient(170deg, #d9d6d4 0%, #b9b6b8 35%, #e4e2e0 65%, #f4f2ef 100%);
  }
  .desk-photo {
    left: 0; top: 0; width: 981px; height: 1391px;
    background: linear-gradient(135deg, #ffffff 40%, #e7ebef 70%, #c9ced6 100%);
    clip-path: polygon(981px 1058px, 981px 1391px, 643px 1391px, 770px 1268px);
  }

  .brand {
    left: 573px; top: 120px; width: 380px; text-align: center;
  }
  .brand-mark {
    width: 60px; height: 60px; margin: 0 auto 14px; background: var(--teal);
  }
  .brand-name {
    font-family: "Montserrat", sans-serif; font-weight: 500;
    font-size: 42px; line-height: 1; color: var(--teal); letter-spacing: -1px;
  }
  .brand-sub {
    margin-top: 4px; font-weight: 500; font-size: 22px; letter-spacing: 10px; color: var(--teal);
  }

  .headline-rule { left: 44px; top: 253px; width: 175px; height: 21px; background: var(--white); }
  .headline {
    left: 44px; top: 310px; width: 500px;
    font-family: "Poppins", sans-serif; font-weight: 700;
    font-size: 61px; line-height: 77px; color: var(--white); letter-spacing: 0.5px;
  }

  .intro {
    left: 44px; top: 831px; width: 900px;
    font-size: 19px; line-height: 23.5px; color: var(--body);
  }
  .intro p + p { margin-top: 23px; }

  .services {
    left: 149px; top: 1006px; list-style: none;
    font-size: 24px; line-height: 30px; color: var(--teal);
  }

  .badge {
    left: 28px; top: 1191px; width: 90px; height: 90px; border-radius: 50%;
    background: var(--white); border: 3px solid #555;
  }
  .badge-caption {
    left: 28px; top: 1296px; width: 90px; text-align: center;
    font-size: 10px; line-height: 13px; color: #333;
  }

  .credentials {
    left: 147px; top: 1228px; display: flex; align-items: center; gap: 10px;
    font-family: "Poppins", sans-serif; font-weight: 600; font-size: 20px; color: var(--ink);
  }
  .diamond { width: 18px; height: 18px; transform: rotate(45deg); margin: 0 6px; }
  .diamond--grey { background: var(--grey); }
  .diamond--teal { background: var(--teal); }

  .phone { left: 182px; top: 1258px; display: flex; align-items: center; gap: 12px; }
  .phone-icon { width: 42px; height: 42px; }
  .phone-number {
    font-family: "Poppins", sans-serif; font-weight: 700; font-size: 62px; line-height: 1; color: var(--ink);
    letter-spacing: 1px;
  }

  .web-band { left: 0; top: 1328px; }
  .web-address {
    left: 28px; top: 1338px; font-size: 29px; color: var(--white); letter-spacing: 0.2px;
  }
</style>
</head>
<body>
<div class="stage">
  <div class="flyer">
    <div class="abs hero-photo" role="img" aria-label="Photo of a woman in a striped shirt working at a desk with a calculator, charts and glasses"></div>
    <div class="abs desk-photo" role="img" aria-label="Photo of hands using a calculator with financial charts"></div>

    <svg class="shape-layer" viewBox="0 0 981 1391" aria-hidden="true">
      <polygon points="0,0 410,0 552,142 0,142" fill="var(--grey)"/>
      <polygon points="0,143 551,143 551,728 65,728 0,663" fill="var(--teal)"/>
      <polygon points="0,968 120,1083 0,1203" fill="var(--teal)"/>
      <polygon points="0,1203 95,1108 107,1120 0,1227" fill="var(--grey)"/>
      <polygon points="981,993 981,1050 758,1273 729,1243" fill="var(--grey)"/>
      <polygon points="0,1328 705,1328 643,1391 0,1391" fill="var(--teal)"/>
    </svg>

    <div class="abs brand">
      <div class="brand-mark"></div>
      <div class="brand-name">EVEN LEDGER</div>
      <div class="brand-sub">Financial Services</div>
    </div>

    <div class="abs headline-rule"></div>
    <h1 class="abs headline">BOOKKEEPING TAILORED TO YOUR BUSINESS NEEDS</h1>

    <div class="abs intro">
      <p>Are you a small business owner, tradie or PAVC Service Provider struggling to stay on top of your bookkeeping and compliance obligations? If so we would love to help you get back on track and take control of your business finances so that you can make informed business decisions and focus on what you do best.</p>
      <p>We have over 20 years industry experience and, as a small business ourselves, we are able to offer our clients a personal bookkeeping solution tailored to meet the needs of your business.</p>
    </div>

    <ul class="abs services">
      <li>Accounts Payable | Accounts Receivable</li>
      <li>Customer Invoicing</li>
      <li>Bank and Credit Card Reconciliations</li>
      <li>Payroll | Superannuation | Payroll Tax</li>
      <li>Business Activity | Instalment Activity Statements</li>
      <li>Regular Financial Reports</li>
      <li>Ledgra and Tallybook Set-Up and Training</li>
    </ul>

    <div class="abs badge"></div>
    <div class="abs badge-caption">BAS agent<br>90123456</div>

    <div class="abs credentials">
      <span class="diamond diamond--grey"></span>
      <span>Ledgra Certified Advisor</span>
      <span class="diamond diamond--teal"></span>
      <span>Tallybook Pro Advisor</span>
    </div>

    <div class="abs phone">
      <svg class="phone-icon" viewBox="0 0 42 42" aria-hidden="true">
        <circle cx="21" cy="21" r="21" fill="var(--teal)"/>
        <path d="M15 11c1 0 2 3 2.6 4.5.3.8-1.4 2.2-1.4 2.6 0 1.6 4.3 6 6 6 .5 0 1.8-1.7 2.6-1.4 1.5.6 4.3 1.6 4.3 2.6 0 1.8-2 4.6-4.4 4.6C21 30 12 21.5 12 15c0-2.3 2.2-4 3-4z" fill="var(--white)"/>
      </svg>
      <span class="phone-number">0400 123 456</span>
    </div>

    <div class="abs web-address">www.evenledgerfinancialservices.com.au</div>
  </div>
</div>
</body>
</html>
```